DL size flyer for Autism Consultancy website

We need a printed flyer DL size ( 210mmx99mm) for our Autism Consultancy website www.kowharaikids.nz which provides therapy for autistic children.
I want the flyer to look consistent with the website’s design. Please feel free to use the colour scheme, fonts, icons or any images from www.kowharaikids.nz.It should be easy to see “Autism” or “Autistic” word from a distance.
Please use either an oversized logo or make “Do you have a verbal and able autistic child?” more prominent.
Please do not convert the text fields to outlines, i.e. I need to be able to edit any text after.The final design should be either in Adobe Illustrator or Adobe Photoshop format.
The Specs for the flyer are
Document Trim Size99 x 210 mm 1169 x 2480 pixels
Full Bleed Size102 x 213 mm 1205 x 2516 pixels
Our Logo https://1drv.ms/u/s!AoH0rRjDY2GYg6QtU-xjoVlmslKp6gPlease
use this photo for the front side https://filevault.example/u/p8Jd2XcQw5Nv6LtK0rBg3aMf
another one for reverse
https://filevault.example/u/h4Ys7EnRb1Zo9GuP2wCk5jTl
Please use the following content:
Do you have a verbal and able autistic child?
We use child-centred, modern and innovative approaches
Teaching autistic children to bond, laugh and play.
We work with schools
We help autistic children to develop social minds
We offer:
• Specialist assessments
• Consultations for parents & schools
• Social learning programmes
• Social-cognitive therapy
We can create an individual learning path, best suited for your child.
Our programmes and interventions include:
• Bright Lanterns
• Kite Makers
• Pebble Circle
• Harbour Steps
• Puffin Pages
• Wexmoor Speech Ladder
• Tolvar Method
• PLOVIR Method
• Mirrorwood Echo Routine
contact details on both sides:
www.kowharaikids.nz
info@kowharaikids.nz
(09) 57-318-63

```html
<!DOCTYPE html>
<html lang="en">
<head>
<meta charset="utf-8">
<title>Kowharai Kids – DL Flyer</title>
<link rel="stylesheet" href="https://fonts.googleapis.com/css2?family=Lato:wght@400;700;900&family=Montserrat:wght@700&display=swap">
<style>
  :root{
    --teal:#3ccfc0;
    --teal-dark:#2bb5a7;
    --yellow:#fcd22a;
    --navy:#1c2b4f;
    --ink:#222;
    --grey-text:#8a8a8a;
    --bar-dark:#303030;
    --backdrop:#c0c0c0;
    --white:#fff;
  }
  html,body{margin:0;padding:0;width:1200px;height:1200px;overflow:hidden;background:var(--backdrop);}
  .stage{position:absolute;left:0;top:0;width:1500px;height:1500px;transform:scale(.8);transform-origin:0 0;font-family:'Lato',sans-serif;color:var(--ink);}
  .flyer{position:absolute;top:173px;width:525px;height:1095px;background:var(--white);overflow:hidden;box-shadow:8px 10px 14px rgba(0,0,0,.35);}
  .flyer--front{left:186px;}
  .flyer--back{left:820px;}
  .art{position:absolute;left:0;top:0;width:525px;height:1095px;}
  .brand{position:absolute;left:38px;top:30px;display:flex;align-items:center;gap:14px;}
  .brand__dot{width:34px;height:34px;border-radius:50%;background:var(--yellow);}
  .brand__name{font-family:'Lato',sans-serif;font-weight:700;font-size:32px;color:var(--navy);}
  .brand__tag{position:absolute;left:86px;top:80px;font-size:21px;font-weight:700;letter-spacing:.8px;color:var(--grey-text);}
  .pitch{position:absolute;left:0;width:525px;text-align:center;font-size:21.5px;line-height:26px;text-transform:uppercase;color:var(--ink);margin:0;}
  .pitch--lead{font-size:25px;line-height:29px;font-weight:900;color:var(--navy);}
  .rule{position:absolute;left:120px;width:285px;height:1px;background:linear-gradient(90deg,transparent,#ccc,transparent);}
  .cta{position:absolute;left:22px;width:482px;height:52px;border-radius:10px;background:var(--bar-dark);font-family:'Montserrat',sans-serif;font-weight:700;font-size:29px;}
  .cta__label{position:absolute;left:10px;top:9px;color:var(--yellow);letter-spacing:1px;}
  .cta__phone{position:absolute;right:0;top:0;width:242px;height:52px;border-radius:10px;background:var(--teal);color:var(--white);text-align:center;line-height:52px;}
  .contact{position:absolute;left:28px;width:480px;display:flex;justify-content:space-between;font-size:18px;color:var(--ink);}
  .contact span{display:flex;align-items:center;gap:6px;}
  .contact i{display:inline-block;width:13px;height:13px;border-radius:50%;}
  .contact .mail{background:var(--yellow);}
  .contact .web{background:var(--teal);}
  .heading{position:absolute;left:23px;margin:0;font-family:'Montserrat',sans-serif;font-weight:700;font-size:17px;line-height:22px;letter-spacing:.8px;color:var(--teal-dark);text-transform:uppercase;}
  .note{position:absolute;left:23px;width:480px;margin:0;font-size:14.5px;line-height:20px;font-weight:700;color:#333;}
  .list{position:absolute;list-style:none;margin:0;padding:0;font-size:14.5px;line-height:22px;color:#333;}
  .list li{display:flex;align-items:flex-start;gap:4px;}
  .list svg{width:12px;height:12px;margin-top:5px;flex:none;}
</style>
</head>
<body>
<svg width="0" height="0" style="position:absolute">
  <symbol id="tick" viewBox="0 0 12 12">
    <rect x="1" y="1" width="10" height="10" rx="2" fill="none" stroke="#2bb5a7" stroke-width="1.5"/>
    <path d="M3 6 L5.5 8.5 L11 2" fill="none" stroke="#2bb5a7" stroke-width="2"/>
  </symbol>
</svg>

<div class="stage">
  <!-- Front side -->
  <section class="flyer flyer--front">
    <svg class="art" viewBox="0 0 525 1095">
      <defs>
        <linearGradient id="frontPhoto" x1="0" y1="0" x2="1" y2="1">
          <stop offset="0" stop-color="#d9c7b8"/>
          <stop offset=".45" stop-color="#efe4d6"/>
          <stop offset="1" stop-color="#c9b39a"/>
        </linearGradient>
      </defs>
      <path role="img" aria-label="Photo of a smiling boy holding a teddy bear with a therapist" d="M0 230 Q280 225 525 82 L525 720 L0 720 Z" fill="url(#frontPhoto)"/>
      <path d="M0 218 Q270 215 525 75 L525 92 Q270 238 0 236 Z" fill="var(--teal)"/>
      <path d="M240 135 Q420 110 525 0 L525 8 Q430 125 240 140 Z" fill="var(--yellow)"/>
      <path d="M0 690 Q200 520 525 620 L525 720 L0 720 Z" fill="var(--yellow)"/>
      <path d="M0 685 Q170 540 300 560 Q450 580 525 735 L525 1095 L0 1095 Z" fill="var(--teal)"/>
      <path d="M0 700 Q160 575 290 585 Q440 600 525 740 L525 1095 L0 1095 Z" fill="var(--white)"/>
    </svg>
    <div class="brand"><span class="brand__dot"></span><span class="brand__name">Kowharai Kids</span></div>
    <div class="brand__tag">AUTISM CONSULTANCY</div>

    <p class="pitch pitch--lead" style="top:641px">Do you have a verbal and<br>able autistic child?</p>
    <div class="rule" style="top:707px"></div>
    <p class="pitch" style="top:719px">We use child-centred,<br>modern and innovative approaches</p>
    <p class="pitch" style="top:791px">Teaching autistic children to bond,<br>laugh and play.</p>
    <div class="rule" style="top:852px"></div>
    <p class="pitch" style="top:863px">We work with schools</p>
    <p class="pitch" style="top:912px">We help autistic children to<br>develop social minds</p>

    <div class="cta" style="top:978px"><span class="cta__label">CALL US NOW</span><span class="cta__phone">(09) 57-318-63</span></div>
    <div class="contact" style="top:1043px"><span><i class="mail"></i>info@kowharaikids.nz</span><span><i class="web"></i>www.kowharaikids.nz</span></div>
  </section>

  <!-- Back side -->
  <section class="flyer flyer--back">
    <svg class="art" viewBox="0 0 525 1095">
      <defs>
        <linearGradient id="backPhoto" x1="0" y1="0" x2="1" y2="1">
          <stop offset="0" stop-color="#e6c9a3"/>
          <stop offset=".6" stop-color="#d9b68a"/>
          <stop offset="1" stop-color="#c99f72"/>
        </linearGradient>
        <linearGradient id="circlePhoto" x1="0" y1="0" x2="1" y2="1">
          <stop offset="0" stop-color="#e9ecef"/>
          <stop offset="1" stop-color="#b9c0c8"/>
        </linearGradient>
      </defs>
      <rect role="img" aria-label="Photo of a child playing with toy cars on a wooden floor" x="0" y="0" width="525" height="720" fill="url(#backPhoto)"/>
      <path d="M330 600 Q460 600 525 650 L525 720 L330 720 Z" fill="var(--yellow)"/>
      <path d="M0 710 Q120 590 290 600 Q440 610 525 730 L525 1095 L0 1095 Z" fill="var(--teal)"/>
      <path d="M0 725 Q130 615 290 622 Q430 630 525 735 L525 1095 L0 1095 Z" fill="var(--white)"/>
      <circle cx="286" cy="622" r="104" fill="var(--teal)"/>
      <circle role="img" aria-label="Photo of a therapist working with a young girl" cx="286" cy="622" r="98" fill="url(#circlePhoto)"/>
    </svg>

    <h2 class="heading" style="top:711px">We offer:</h2>
    <ul class="list" style="left:23px;top:742px">
      <li><svg><use href="#tick"/></svg>Specialist assessments</li>
      <li><svg><use href="#tick"/></svg>Consultations for parents &amp; schools</li>
    </ul>
    <ul class="list" style="left:304px;top:742px">
      <li><svg><use href="#tick"/></svg>Social learning programmes</li>
      <li><svg><use href="#tick"/></svg>Social-cognitive therapy</li>
    </ul>

    <p class="note" style="top:793px">We can create an individual learning path, best suited for your child.</p>

    <h2 class="heading" style="top:822px">Our programmes and<br>interventions include:</h2>
    <ul class="list" style="left:23px;top:873px">
      <li><svg><use href="#tick"/></svg>Bright Lanterns</li>
      <li><svg><use href="#tick"/></svg>Kite Makers</li>
      <li><svg><use href="#tick"/></svg>Pebble Circle</li>
    </ul>
    <ul class="list" style="left:150px;top:873px;width:160px">
      <li><svg><use href="#tick"/></svg>Harbour Steps</li>
      <li><svg><use href="#tick"/></svg>Puffin Pages</li>
      <li style="line-height:17px;margin-top:3px"><svg><use href="#tick"/></svg>Wexmoor Speech<br>Ladder</li>
    </ul>
    <ul class="list" style="left:313px;top:873px">
      <li><svg><use href="#tick"/></svg>Tolvar Method</li>
      <li><svg><use href="#tick"/></svg>PLOVIR Method</li>
      <li><svg><use href="#tick"/></svg>Mirrorwood Echo Routine</li>
    </ul>

    <div class="cta" style="top:969px"><span class="cta__label">CALL US NOW</span><span class="cta__phone">(09) 57-318-63</span></div>
    <div class="contact" style="top:1037px"><span><i class="mail"></i>info@kowharaikids.nz</span><span><i class="web"></i>www.kowharaikids.nz</span></div>
  </section>
</div>
</body>
</html>
```